Stationary and Business Card for Law Firm
Modern, Professional & Sophisticated Law Firm Card
Stationary and Business Card for Law Firm - Law
Creative Brief
Professional
Owen Barker
Partner
482 North Mill Avenue Pelham, Illinois 62904
obarker@barkerwynn.example
www.barkerwynn.example
These cards will be used by three attorneys, so I would like to be able to change the names out. Alternatively, if you could insert the names when providing source files, it would be appreciated. Names are: Owen B. Barker Rosalind P. Barker Natalie K. Wynn Emails are: obarker@barkerwynn.example rbarker@barkerwynn.example nwynn@barkerwynn.example
pbruner27 pbruner27
While I like the look many of the envelopes, the return address must be in the upper right hand corner to meet US Postal regulations. Firm Name/Logo Address City, State Zip (additional design info if you like) I have had similar envelopes on a different project with the Logo address on the lower part of the envelope---the post office refused to accept them.

```html
<!DOCTYPE html>
<html lang="en">
<head>
<meta charset="utf-8">
<title>Barker &amp; Wynn — Business Card</title>
<link rel="stylesheet" href="https://fonts.googleapis.com/css2?family=Cinzel:wght@400&family=Marcellus&family=Open+Sans:wght@400&display=swap">
<style>
  :root {
    --backdrop: #2e2e2e;
    --card-white: #ffffff;
    --card-black: #141414;
    --gold: #b0946a;
    --ink: #3a3a3a;
    --ink-soft: #6b6b6b;
    --rule: #c9c9c9;
    --on-black: #f2f2f2;
  }
  * { box-sizing: border-box; margin: 0; padding: 0; }
  html, body {
    width: 1200px; height: 901px; overflow: hidden;
    background: var(--backdrop);
  }
  .canvas {
    width: 1200px; height: 901px;
    display: flex; align-items: center; justify-content: center; gap: 60px;
  }
  .card {
    width: 520px; height: 297px;
    position: relative;
    box-shadow: 0 10px 30px rgba(0,0,0,.45);
  }

  /* Front */
  .card-front { background: var(--card-white); display: flex; align-items: center; }
  .brand-block {
    width: 235px; height: 100%;
    display: flex; flex-direction: column; align-items: center; justify-content: center;
  }
  .brand-mark {
    width: 44px; height: 44px; background: var(--gold); margin-bottom: 14px;
  }
  .brand-name {
    font-family: "Cinzel", serif; font-size: 22px; letter-spacing: 1px; color: var(--ink);
  }
  .brand-tagline {
    font-family: "Cinzel", serif; font-size: 8px; letter-spacing: 2px; color: var(--ink-soft);
    margin-top: 4px;
  }
  .divider { width: 1px; height: 190px; background: var(--rule); }
  .contact-block { padding-left: 26px; }
  .person-name {
    font-family: "Marcellus", serif; font-size: 22px; letter-spacing: 1.5px; color: var(--gold);
    text-transform: uppercase;
  }
  .person-title {
    font-family: "Open Sans", sans-serif; font-size: 10px; color: var(--ink-soft); margin: 2px 0 12px;
  }
  .address, .contact-line {
    font-family: "Open Sans", sans-serif; font-size: 10.5px; color: var(--ink); line-height: 1.55;
  }
  .address { margin-bottom: 8px; }
  .contact-line { display: flex; align-items: center; gap: 7px; }
  .contact-line svg { flex: none; }

  /* Back */
  .card-back {
    background: var(--card-black);
    display: flex; flex-direction: column; align-items: center; justify-content: center;
  }
  .back-name {
    font-family: "Cinzel", serif; font-size: 34px; letter-spacing: 1.5px; color: var(--on-black);
  }
  .back-tagline {
    font-family: "Cinzel", serif; font-size: 11px; letter-spacing: 3px; color: var(--on-black);
    margin-top: 4px;
  }
</style>
</head>
<body>
<main class="canvas">
  <section class="card card-front">
    <div class="brand-block">
      <div class="brand-mark"></div>
      <div class="brand-name">BARKER &amp; WYNN</div>
      <div class="brand-tagline">ATTORNEYS AT LAW</div>
    </div>
    <div class="divider"></div>
    <div class="contact-block">
      <div class="person-name">Owen Barker</div>
      <div class="person-title">Partner</div>
      <div class="address">482 North Mill Avenue<br>Pelham, Illinois 62904</div>
      <div class="contact-line">
        <svg width="9" height="9" viewBox="0 0 10 10"><circle cx="5" cy="5" r="5" fill="var(--gold)"/></svg>
        217.555.0142
      </div>
      <div class="contact-line">
        <svg width="9" height="9" viewBox="0 0 10 10"><circle cx="5" cy="5" r="5" fill="var(--gold)"/></svg>
        217.555.0187
      </div>
      <div class="contact-line">
        <svg width="9" height="9" viewBox="0 0 10 10"><circle cx="5" cy="5" r="5" fill="var(--gold)"/></svg>
        obarker@barkerwynn.example
      </div>
      <div class="contact-line">
        <svg width="9" height="9" viewBox="0 0 10 10"><circle cx="5" cy="5" r="5" fill="var(--gold)"/></svg>
        www.barkerwynn.example
      </div>
    </div>
  </section>

  <section class="card card-back">
    <div class="back-name">BARKER &amp; WYNN</div>
    <div class="back-tagline">ATTORNEYS AT LAW</div>
  </section>
</main>
</body>
</html>
```